New Business Card for Web Design/Internet Marketing Company

Looking for a great looking new business card. We are a 10 year old web design, internet marketing and website management company that works mostly with small businesses.

Our new card needs to better match the colors and style of our website, be bold, extremely usable and slightly edgy.

Target Market(s)

Small/Medium businesses that have websites

Industry/Entity Type

Internet

Requirements
Must have
• Front and back design, full color, rounded corners please

Must use the colors/style of our website (JPG provided)

INFO FOR CARDS (as readable as possible please)
Dana Okafor
President/CEO
dana@brivatnet.example
Phone: 520-555-0143
Toll Free: 800-555-0178
Address: 4125 W. Larkspur Ave. Ste. 160, Tucson, AZ 85799

THINGS I WANT TO PROMOTE (if there is room):
1. Our Website - www.brivatnet.example

2. Social Media
Twitter: @brivatnet
Facebook: www.facebook.com/brivatnet

3. Our Services
Web Design
Internet Marketing
Website Management

```html
<!DOCTYPE html>
<html lang="en">
<head>
<meta charset="utf-8">
<title>Brivatnet Business Card</title>
<link href="https://fonts.googleapis.com/css2?family=Cabin:wght@400;600;700&display=swap" rel="stylesheet">
<style>
  :root {
    --backdrop: #e8e5e1;
    --card-white: #ffffff;
    --panel-grey: #58595b;
    --accent-blue: #0a8cc8;
    --brand-orange: #f28a30;
    --text-light: #ffffff;
    --text-dark: #4a4b4d;
  }
  * { margin: 0; padding: 0; box-sizing: border-box; }
  html, body { width: 1200px; height: 402px; overflow: hidden; }
  body {
    background: var(--backdrop);
    font-family: "Cabin", "Trebuchet MS", sans-serif;
    position: relative;
  }
  .card {
    position: absolute;
    top: 56px;
    width: 513px;
    height: 292px;
    background: var(--card-white);
    border-radius: 6px;
    overflow: hidden;
    box-shadow: 0 2px 8px rgba(0,0,0,.18);
  }
  .card--front { left: 70px; }
  .card--back { left: 619px; }
  .card__shapes { position: absolute; inset: 0; width: 100%; height: 100%; }
  .shape-blue { fill: var(--accent-blue); }
  .shape-grey { fill: var(--panel-grey); }
  .icon-cut { fill: var(--panel-grey); }
  .icon-line { stroke: var(--panel-grey); fill: none; }
  .icon { fill: var(--text-light); }

  .brand-name {
    position: absolute;
    color: var(--brand-orange);
    font-weight: 700;
    letter-spacing: -0.5px;
    line-height: 1;
  }
  .card--front .brand-name { left: 26px; top: 160px; font-size: 44px; }
  .card--back .brand-name { left: 63px; top: 112px; font-size: 54px; }

  .contact {
    position: absolute;
    right: 30px;
    text-align: right;
    color: var(--text-light);
    white-space: nowrap;
  }
  .contact__name { top: 25px; font-size: 19px; font-weight: 700; line-height: 24px; }
  .contact__title { top: 47px; font-size: 12px; line-height: 16px; }
  .contact__address { top: 104px; font-size: 13px; line-height: 17.5px; }
  .contact__lines { top: 196px; font-size: 12.5px; line-height: 17.5px; }
  .contact__lines li { list-style: none; display: flex; justify-content: flex-end; align-items: center; gap: 4px; }
  .contact__lines svg { width: 9px; height: 9px; flex: none; }

  .social {
    position: absolute;
    left: 76px;
    top: 207px;
    font-size: 13px;
    line-height: 18px;
    color: var(--text-dark);
  }
  .social li { list-style: none; display: flex; align-items: center; gap: 6px; }
  .social__mark { width: 11px; height: 11px; background: var(--accent-blue); border-radius: 2px; flex: none; }

  .services {
    position: absolute;
    right: 24px;
    top: 139px;
    text-align: right;
    color: var(--text-light);
    white-space: nowrap;
  }
  .services__heading { font-size: 19px; font-weight: 600; line-height: 24px; margin-bottom: 21px; }
  .services__list li { list-style: none; font-size: 17px; line-height: 27px; }
</style>
</head>
<body>

<section class="card card--front">
  <svg class="card__shapes" viewBox="0 0 513 292" preserveAspectRatio="none" aria-hidden="true">
    <path class="shape-blue" d="M296 0 C336 100 300 222 193 292 L208 292 C318 222 352 100 330 0 Z"/>
    <path class="shape-grey" d="M330 0 C352 100 318 222 208 292 L513 292 L513 0 Z"/>
  </svg>

  <div class="brand-name">brivatnet</div>

  <div class="contact contact__name">Dana Okafor</div>
  <div class="contact contact__title">President/CEO</div>
  <div class="contact contact__address">
    4125 W. Larkspur Ave.<br>Ste. 160<br>Tucson, AZ 85799
  </div>
  <ul class="contact contact__lines">
    <li>520-555-0143
      <svg viewBox="0 0 10 10"><circle class="icon" cx="5" cy="5" r="5"/><path class="icon-cut" d="M3 2.5 L4.2 2.5 L4.6 4 L3.9 4.6 Q4.6 5.9 5.6 6.3 L6.2 5.6 L7.6 6 L7.6 7.2 Q4 7.6 3 2.5Z"/></svg>
    </li>
    <li>800-555-0178
      <svg viewBox="0 0 10 10"><circle class="icon" cx="5" cy="5" r="5"/><path class="icon-cut" d="M3 2.5 L4.2 2.5 L4.6 4 L3.9 4.6 Q4.6 5.9 5.6 6.3 L6.2 5.6 L7.6 6 L7.6 7.2 Q4 7.6 3 2.5Z"/></svg>
    </li>
    <li>dana@brivatnet.example
      <svg viewBox="0 0 10 10"><rect class="icon" x="0.5" y="2" width="9" height="6.5"/><path class="icon-line" d="M0.5 2 L5 5.5 L9.5 2" stroke-width="0.9"/></svg>
    </li>
    <li>www.brivatnet.example
      <svg viewBox="0 0 10 10"><circle class="icon" cx="5" cy="5" r="5"/><path class="icon-line" d="M0 5 H10 M5 0 V10 M5 0 Q1.5 5 5 10 M5 0 Q8.5 5 5 10" stroke-width="0.7"/></svg>
    </li>
  </ul>
</section>

<section class="card card--back">
  <svg class="card__shapes" viewBox="0 0 512 292" preserveAspectRatio="none" aria-hidden="true">
    <path class="shape-blue" d="M297 0 C338 100 302 222 195 292 L210 292 C320 222 354 100 331 0 Z"/>
    <path class="shape-grey" d="M331 0 C354 100 320 222 210 292 L512 292 L512 0 Z"/>
  </svg>

  <div class="brand-name">brivatnet</div>

  <ul class="social">
    <li><span class="social__mark"></span>@brivatnet</li>
    <li><span class="social__mark"></span>brivatnet</li>
  </ul>

  <div class="services">
    <h2 class="services__heading">Our Services</h2>
    <ul class="services__list">
      <li>Web Design</li>
      <li>Internet Marketing</li>
      <li>Website Management</li>
    </ul>
  </div>
</section>

</body>
</html>
```